Business Card for Polygraph business in Africa

Business Card . Polygraph Examiner based in Tanzania, East Africa.
Business Card will be used to disseminate contact information to potential clients.
It should convey that I am a professional specifically in the polygraph field and perform my work with integrity.

I have attached the business card that I'm currently using, which I threw together myself initially. It's not professional enough.

Target Market(s)

Banks, Accounting Firms, Government Ministries, Gas, Oil, & Gemstone Mining Concerns, Wildlife Conservation NGOs, International companies located in East Africa.

Industry/Entity Type

Business

Contact Information for Business Card

Veritrace Kilanga
Miriam Ostbrook
PO Box 48731
Arusha, Tanzania
+255 684 219 537
miriamostbrook@mailvera.example

Colors
00a990
f37122
faa54b

Requirements
Must have
• - Veritrace Kilanga (with the word "Polygraph" being more prominent than the word "Tanzania")
• - Forensic Examinations
• - Employment Screening
• - Should contain a logo of the Continental Truthtrace Society (of which I'm a member)
• - I would like an accent design (such as the polygraph "squiggles" of a cardio tracing or such as that)
• - My contact information (less prominent, but large enough to read legibly). I would also consider putting the contact information on the second side of the card.
Nice to have
• My color suggestions are changeable.
Should not have
• Anything "cutesy" or "cartoonish"

```html
<!DOCTYPE html>
<html lang="en">
<head>
<meta charset="utf-8">
<title>Veritrace Kilanga — Business Card</title>
<link rel="stylesheet" href="https://fonts.googleapis.com/css2?family=Montserrat:wght@400;500;700&display=swap">
<style>
  :root {
    --backdrop: #2a2a2a;
    --card: #050505;
    --card-sheen: #1c1c1c;
    --ink: #f2f2f2;
    --orange: #f37122;
    --teal: #00a990;
  }
  * { margin: 0; padding: 0; box-sizing: border-box; }
  html, body {
    width: 1200px; height: 930px; overflow: hidden;
    background: var(--backdrop);
    font-family: "Montserrat", Arial, sans-serif;
  }
  .card {
    position: absolute; left: 260px;
    width: 680px; height: 400px;
    border-radius: 24px; overflow: hidden;
    background: linear-gradient(115deg, var(--card) 0%, var(--card) 38%, var(--card-sheen) 52%, var(--card) 70%);
  }
  .card--front { top: 45px; }
  .card--back { top: 485px; }

  .brand {
    position: absolute; display: flex; align-items: center; gap: 10px;
    font-weight: 700; font-size: 26px; color: var(--orange); letter-spacing: 0.3px;
  }
  .brand__dot { width: 14px; height: 14px; border-radius: 50%; background: var(--teal); }
  .card--front .brand { left: 70px; top: 215px; }
  .card--back .brand { left: 50px; top: 165px; font-size: 24px; }

  .member-badge { position: absolute; right: 60px; top: 45px; }

  .divider {
    position: absolute; left: 345px; top: 95px;
    width: 2px; height: 150px; background: var(--orange);
  }
  .contact { position: absolute; left: 372px; top: 100px; color: var(--ink); }
  .contact__name {
    font-weight: 500; font-size: 26px; color: var(--orange);
    text-transform: uppercase; letter-spacing: 1px; margin-bottom: 10px;
  }
  .contact__line { font-size: 15px; line-height: 22px; }
  .contact__row { display: flex; align-items: center; gap: 10px; font-size: 15px; line-height: 24px; }
  .contact__row:first-of-type { margin-top: 8px; }
  .contact__icon { width: 12px; height: 12px; flex: none; }

  .service-band {
    position: absolute; left: 0; bottom: 0; width: 100%; height: 36px; display: flex;
  }
  .service-band__end { background: var(--teal); }
  .service-band__end--left { width: 140px; }
  .service-band__end--right { width: 100px; }
  .service-band__main {
    flex: 1; background: var(--orange); color: var(--ink);
    font-size: 15px; font-weight: 500; text-transform: uppercase; letter-spacing: 0.8px;
    display: flex; align-items: center; justify-content: center;
  }
</style>
</head>
<body>

<section class="card card--front">
  <div class="brand"><span class="brand__dot"></span>Veritrace Kilanga</div>
  <svg class="member-badge" width="120" height="120" viewBox="0 0 120 120" role="img" aria-label="Continental Truthtrace Society membership seal">
    <circle cx="60" cy="60" r="56" fill="#f2f2f2"/>
    <circle cx="60" cy="60" r="40" fill="#050505"/>
  </svg>
</section>

<section class="card card--back">
  <div class="brand"><span class="brand__dot"></span>Veritrace Kilanga</div>
  <div class="divider"></div>
  <div class="contact">
    <div class="contact__name">Miriam Ostbrook</div>
    <div class="contact__line">PO Box 48731</div>
    <div class="contact__line">Arusha, Tanzania</div>
    <div class="contact__row">
      <svg class="contact__icon" viewBox="0 0 12 12" aria-hidden="true"><path d="M2 1 L4.5 1 L5.5 3.5 L4 4.8 Q5 7 7.2 8 L8.5 6.5 L11 7.5 L11 10 Q6 11 2.5 7.5 Q0.5 4.5 2 1 Z" fill="#f37122"/></svg>
      +255 684 219 537
    </div>
    <div class="contact__row">
      <svg class="contact__icon" viewBox="0 0 12 12" aria-hidden="true"><rect x="0.75" y="2.25" width="10.5" height="7.5" fill="none" stroke="#f37122" stroke-width="1.5"/><path d="M1 2.5 L6 6.5 L11 2.5" fill="none" stroke="#f37122" stroke-width="1.5"/></svg>
      miriamostbrook@mailvera.example
    </div>
  </div>
  <div class="service-band">
    <div class="service-band__end service-band__end--left"></div>
    <div class="service-band__main">Issue Investigation - Employment Screening</div>
    <div class="service-band__end service-band__end--right"></div>
  </div>
</section>

</body>
</html>
```